Amazing Homepage required for Ireland's Top Crowdfunding site

Design/ PSD Files required.

BrightHarbour.com is the market leader in crowd lending/peer to peer lending in Ireland. Businesses/SME’s can borrow anything from €5,000 to €100,000 at interest rates much more favourable than those offered by the banks. BH is also a quicker and less bureaucratic than traditional lending institutions. We are a viable alternative to banks and traditional sources of finance.

Our lenders are members of the public and they can lend directly to Irish businesses in amounts from €50 to €2,000. They get a better rate of return than deposit accounts, as well as the feel good factor of supporting a local business.

We have just completed a full rebrand of our logo and colours and would now like to utilise these to best effect by implementing them in a total redesign of our homepage to attract borrowers and lenders. Please see the attached files for the brand guidelines and logo/colours to be used.

We are looking for a designer to utilise our new branding in a creative way, conveying that we are modern, trustworthy, competitive and friendly/local.

We currently have two different user groups:
1- Lenders; this currently consists of members of the public but in future will expand to include financial institutions

2- Business borrowers looking for funds for their business

Embracing and balancing both of these user groups is difficult so we would like the homepage to primarily target borrowers but incorporate clear alternative calls to action for lenders/prospective lenders as well.

We would like:
Infinite scroll homepage
New logo and tagline on a fixed header which should also include; ‘Marketplace’ ‘About’ ‘FAQ’ and a clear login button
A static full bleed image
Overlaid over this we would like a loan calculator in a similar style/functionality to this one on www.quellmoor.com. It should have:
an image of a slider icon with amounts from €0 to €100,000
A text field with ‘Business Loan amount’ which fills when the slider is moved
Then, a text field called ‘Monthly repayment’
An email field with a clear call to action ie ‘Go’ or ‘Get Started’
The purpose of this is to enable prospective borrowers to quickly and easily get a quote estimate for their loan
Underneath this we would like to have an alternate call to action to target prospective lenders; something like ‘Looking to Lend?’

Further down the page we would like to have a heading ‘What is Bright Harbour?’
(include information from company overview)

3 images to illustrate loans live in our Marketplace

Target Market(s)

This Homepge should appeal to small business owners

Industry/Entity Type

Crowd

Number of Pages Required

1 page

Font styles to use
Sans Serif

Requirements
Must have
• Linear clean and modern homepage
• Clear calls to action
Nice to have
• Ideas for how video/rich media might be incorporated into a future iteration of the homepage

```html
<!DOCTYPE html>
<html lang="en">
<head>
<meta charset="utf-8">
<title>Bright Harbour – Business Lending</title>
<link href="https://fonts.googleapis.com/css2?family=Cabin:wght@400;600;700&family=Open+Sans:wght@400;600;700&display=swap" rel="stylesheet">
<style>
:root{
  --red:#e8401c;
  --red-dark:#c8300f;
  --navy:#16294a;
  --grey-text:#666;
  --light-line:#dfe5ec;
  --track:#d3deea;
  --footer:#1d1d1d;
  --footer-bottom:#161616;
  --footer-text:#cfcfcf;
  --white:#fff;
}
*{margin:0;padding:0;box-sizing:border-box}
html,body{width:690px;height:1200px;overflow:hidden;background:#fff}
body{position:relative;font-family:"Open Sans",Arial,sans-serif;color:var(--navy)}
.abs{position:absolute}
.topline{left:0;top:0;width:690px;height:2px;background:var(--red)}
/* header */
.site-header{left:0;top:2px;width:690px;height:63px;background:#fff}
.brand{left:57px;top:18px;display:flex;align-items:center;gap:6px}
.brand-mark{width:16px;height:16px;border-radius:50%;background:var(--red)}
.brand-name{font-family:"Cabin",sans-serif;font-weight:600;font-size:13px;color:var(--navy)}
.brand-tag{left:57px;top:47px;font-size:5.5px;color:var(--red)}
.main-nav{left:224px;top:27px;display:flex;gap:0;font-size:7.5px;color:#333;text-transform:uppercase}
.main-nav span{margin-right:27px}
.main-nav .active{color:var(--red)}
.btn-login{left:573px;top:22px;width:60px;height:21px;background:var(--red);color:#fff;font-family:"Cabin",sans-serif;font-weight:700;font-size:11px;display:flex;align-items:center;justify-content:center;border-radius:2px;box-shadow:0 2px 0 var(--red-dark)}
/* hero */
.hero{left:0;top:65px;width:690px;height:301px;background:linear-gradient(90deg,#1e3550 0%,#516478 35%,#7b8ea1 55%,#8a5e4e 80%,#5a3d35 100%)}
.hero-arrow{top:180px;width:26px;height:26px}
/* calculator */
.calc{left:35px;top:259px;width:620px;height:379px;background:#fff;box-shadow:0 8px 10px -6px rgba(0,0,0,.35)}
.calc-title{left:0;top:24px;width:620px;text-align:center;font-family:"Cabin",sans-serif;font-weight:700;font-size:17px}
.red{color:var(--red)}
.range-label{top:47px;font-family:"Cabin",sans-serif;font-weight:700;font-size:10.5px}
.rule{height:1px;background:var(--light-line)}
.step-num{width:23px;height:23px;border:2px solid var(--navy);border-radius:50%;font-family:"Cabin",sans-serif;font-weight:700;font-size:9px;display:flex;align-items:center;justify-content:center}
.step-label{font-family:"Cabin",sans-serif;font-weight:700;font-size:8.5px;text-transform:uppercase}
.step-hint{font-size:6.5px;color:#555}
.value-box{width:37px;height:23px;border:1px solid var(--light-line);font-size:8px;color:#555;display:flex;align-items:center;justify-content:center}
.result-label{font-size:7.5px;color:#444}
.result-value{font-family:"Cabin",sans-serif;font-weight:700;font-size:16px;color:var(--red)}
.operator{font-family:"Cabin",sans-serif;font-weight:700;font-size:22px;color:var(--navy)}
.btn-cta{width:145px;height:31px;background:linear-gradient(#f05a2a,var(--red-dark));color:#fff;font-family:"Cabin",sans-serif;font-weight:700;font-size:11.5px;display:flex;align-items:center;justify-content:center;border-radius:2px}
.example-title{font-family:"Cabin",sans-serif;font-weight:700;font-size:11.5px}
.example-text{font-size:7.5px;line-height:13px;color:#555;width:400px}
/* about */
.about-title{left:0;top:656px;width:690px;text-align:center;font-family:"Cabin",sans-serif;font-weight:700;font-size:12.5px}
.about-text{left:105px;top:683px;width:480px;text-align:center;font-size:6.5px;line-height:12.5px;color:#555}
.loan-card{top:740px;width:177px;height:230px;background:#fff;border:1px solid #eee;box-shadow:0 7px 6px -5px rgba(0,0,0,.3)}
.loan-photo{position:absolute;left:3px;top:3px;width:170px;height:101px}
.loan-title{position:absolute;left:6px;top:111px;width:165px;font-size:9.5px;line-height:13px;color:#555}
.loan-desc{position:absolute;left:6px;top:140px;width:165px;font-size:6.2px;line-height:11.5px;color:#888}
.loan-amount{position:absolute;left:6px;top:183px;font-size:6.5px;color:#333}
.loan-bar{position:absolute;left:6px;top:194px;width:163px;height:5px;background:#e3e3e3;border-radius:3px;overflow:hidden}
.loan-bar i{display:block;height:100%;background:var(--red);border-radius:3px}
.loan-meta{position:absolute;left:6px;top:204px;width:163px;display:flex;justify-content:space-between;font-size:6.3px;color:#555}
/* footer */
.site-footer{left:0;top:998px;width:690px;height:202px;background:var(--footer);border-top:5px solid #3a3a3a}
.foot-heading{top:1024px;font-family:"Cabin",sans-serif;font-weight:600;font-size:10.5px;color:#fff}
.foot-text{font-size:6px;line-height:12px;color:var(--footer-text)}
.foot-date{color:var(--red)}
.field{width:112px;border:1px solid #ddd;font-size:6px;color:#fff;padding:3px 4px}
.btn-submit{left:577px;top:1130px;width:55px;height:21px;background:var(--red);color:#fff;font-size:7px;display:flex;align-items:center;justify-content:center}
.foot-bottom{left:0;top:1165px;width:690px;height:35px;background:var(--footer-bottom);border-top:1px solid #2c2c2c}
.copyright{left:58px;top:1179px;font-size:6px;color:#bbb}
.social{top:1173px;width:17px;height:17px;border:1px solid #ddd;border-radius:50%}
</style>
</head>
<body>
<div class="abs topline"></div>

<header class="abs site-header"></header>
<div class="abs brand"><span class="brand-mark"></span><span class="brand-name">Bright Harbour</span></div>
<div class="abs brand-tag">the business lending people</div>
<nav class="abs main-nav">
  <span class="active">Home</span><span>Marketplace</span><span>About</span><span>FAQ</span><span>How it work</span><span>Contact us</span>
</nav>
<div class="abs btn-login">LOGIN</div>

<div class="abs hero" role="img" aria-label="Full-bleed photo of a hand pressing a glowing 'Business Loan' button on a virtual screen over a brick wall"></div>
<svg class="abs hero-arrow" style="left:23px" viewBox="0 0 26 26"><circle cx="13" cy="13" r="11.5" fill="none" stroke="#fff" stroke-width="2"/><path d="M16 7 L9 13 L16 19 Z" fill="#fff"/></svg>
<svg class="abs hero-arrow" style="left:639px" viewBox="0 0 26 26"><circle cx="13" cy="13" r="11.5" fill="none" stroke="#fff" stroke-width="2"/><path d="M10 7 L17 13 L10 19 Z" fill="#fff"/></svg>

<section class="abs calc">
  <h2 class="abs calc-title">LOAN <span class="red">CALCULATOR</span></h2>
  <div class="abs range-label" style="left:22px">FROM €0</div>
  <div class="abs range-label red" style="right:22px">TO €100,000</div>
  <div class="abs rule" style="left:22px;top:61px;width:576px"></div>

  <div class="abs step-num" style="left:22px;top:74px">1</div>
  <div class="abs step-label" style="left:50px;top:81px">Business <span class="red">Loan Amount</span></div>
  <div class="abs step-hint" style="left:176px;top:82px">what kind of Protection do you need?</div>
  <div class="abs value-box" style="left:560px;top:74px">£ 111</div>

  <svg class="abs" style="left:20px;top:103px" width="580" height="30" viewBox="0 0 580 30">
    <circle cx="8" cy="15" r="6" fill="#fff" stroke="#555" stroke-width=".8"/><line x1="5" y1="15" x2="11" y2="15" stroke="#555"/>
    <line x1="18" y1="15" x2="560" y2="15" stroke="var(--track)" stroke-width="2.5"/>
    <line x1="18" y1="15" x2="295" y2="15" stroke="var(--navy)" stroke-width="2.5"/>
    <circle cx="295" cy="15" r="12" fill="#fff" stroke="#ddd"/>
    <path d="M292 11 L288 15 L292 19 M298 11 L302 15 L298 19" fill="none" stroke="#333" stroke-width="1.2"/>
    <circle cx="571" cy="15" r="6" fill="#fff" stroke="#555" stroke-width=".8"/><path d="M568 15 H574 M571 12 V18" stroke="#555"/>
  </svg>

  <div class="abs step-num" style="left:22px;top:138px">2</div>
  <div class="abs step-label" style="left:50px;top:145px">Monthly <span class="red">Repayment</span></div>
  <div class="abs step-hint" style="left:175px;top:146px">How many users will be protected?</div>
  <div class="abs value-box" style="left:560px;top:138px">£ 111</div>

  <svg class="abs" style="left:20px;top:167px" width="580" height="30" viewBox="0 0 580 30">
    <circle cx="8" cy="15" r="6" fill="#fff" stroke="#555" stroke-width=".8"/><line x1="5" y1="15" x2="11" y2="15" stroke="#555"/>
    <line x1="18" y1="15" x2="560" y2="15" stroke="var(--track)" stroke-width="2.5"/>
    <line x1="18" y1="15" x2="474" y2="15" stroke="var(--navy)" stroke-width="2.5"/>
    <circle cx="474" cy="15" r="12" fill="#fff" stroke="#ddd"/>
    <path d="M471 11 L467 15 L471 19 M477 11 L481 15 L477 19" fill="none" stroke="#333" stroke-width="1.2"/>
    <circle cx="571" cy="15" r="6" fill="#fff" stroke="#555" stroke-width=".8"/><path d="M568 15 H574 M571 12 V18" stroke="#555"/>
  </svg>

  <div class="abs rule" style="left:22px;top:215px;width:576px"></div>

  <div class="abs result-label" style="left:41px;top:238px">Borrowing</div>
  <div class="abs result-value" style="left:41px;top:247px">£111</div>
  <div class="abs operator" style="left:115px;top:241px">+</div>
  <div class="abs result-label" style="left:172px;top:238px">Interest</div>
  <div class="abs result-value" style="left:172px;top:247px">£22.20</div>
  <div class="abs operator" style="left:254px;top:241px">=</div>
  <div class="abs result-label" style="left:305px;top:238px">Total to repay</div>
  <div class="abs result-value" style="left:305px;top:247px">£133.20</div>
  <div class="abs btn-cta" style="left:430px;top:236px">GET STARTED</div>

  <div class="abs rule" style="left:22px;top:287px;width:576px"></div>

  <div class="abs example-title" style="left:29px;top:298px">REPRESENTATIVE <span class="red">EXAMPLE</span></div>
  <p class="abs example-text" style="left:29px;top:317px">Businesses/SME’s can borrow anything from <b style="color:var(--navy)">€5,000 to €100,000</b> at interest rates much more favourable than those offered by the banks.</p>
  <div class="abs btn-cta" style="left:430px;top:302px">LOOKING TO LEND?</div>
</section>

<h2 class="abs about-title">WHAT IS <span class="red">BRIGHT HARBOUR?</span></h2>
<p class="abs about-text">BrightHarbour has borrowers from different industries and sectors. Some companies have been established longer than others. Some sell to consumers, while others may only supply businesses.To make your lending decision easier and to help you build up a lending portfolio that suits you, we have developed the CMYK system to group the four categories of borrower. Here’s how it works.</p>

<article class="abs loan-card" style="left:57px">
  <div class="loan-photo" role="img" aria-label="Photo of a hand signing a loan document with a pen" style="background:linear-gradient(135deg,#2d4a6e,#9fb8d0 60%,#e6eef5)"></div>
  <h3 class="loan-title" style="font-weight:400">Can anyone become a lender at BrightHarbour?</h3>
  <p class="loan-desc">We review each potential borrower and we only allow businesses to borrow if they have successfully completed a full, rigorous credit vetting process.</p>
  <div class="loan-amount">€5,000 USD</div>
  <div class="loan-bar"><i style="width:50%"></i></div>
  <div class="loan-meta"><span>50%</span><span>45 Days Left</span></div>
</article>
<article class="abs loan-card" style="left:257px">
  <div class="loan-photo" role="img" aria-label="Photo of business people shaking hands across a meeting table" style="background:linear-gradient(135deg,#c9d4dc,#6f7c88 55%,#2f3a44)"></div>
  <h3 class="loan-title" style="font-weight:400">Can anyone become a lender at BrightHarbour?</h3>
  <p class="loan-desc">We review each potential borrower and we only allow businesses to borrow if they have successfully completed a full, rigorous credit vetting process.</p>
  <div class="loan-amount">€5,000 USD</div>
  <div class="loan-bar"><i style="width:78%"></i></div>
  <div class="loan-meta"><span>78%</span><span>45 Days Left</span></div>
</article>
<article class="abs loan-card" style="left:456px">
  <div class="loan-photo" role="img" aria-label="Photo of a couple reviewing loan papers with an adviser" style="background:linear-gradient(135deg,#b9c3c9,#8b7565 50%,#3d3733)"></div>
  <h3 class="loan-title" style="font-weight:400">Can anyone become a lender at BrightHarbour?</h3>
  <p class="loan-desc">We review each potential borrower and we only allow businesses to borrow if they have successfully completed a full, rigorous credit vetting process.</p>
  <div class="loan-amount">€5,000 USD</div>
  <div class="loan-bar"><i style="width:95%"></i></div>
  <div class="loan-meta"><span>95%</span><span>45 Days Left</span></div>
</article>

<footer class="abs site-footer"></footer>
<h4 class="abs foot-heading" style="left:58px">Contact Us</h4>
<p class="abs foot-text" style="left:58px;top:1041px;font-size:4.5px;line-height:12px">Fusce dapibus, tellus ac cursus commodo tortor mauris.<br>Fusce dapibus, tellus magna.</p>
<svg class="abs" style="left:58px;top:1092px" width="8" height="48" viewBox="0 0 8 48">
  <path d="M4 1 A3 3 0 0 1 7 4 C7 6 4 9 4 9 C4 9 1 6 1 4 A3 3 0 0 1 4 1 Z" fill="var(--red)"/>
  <path d="M1 24 Q4 20 7 24 L6 26 H2 Z" fill="var(--red)"/>
  <rect x="1" y="36" width="6" height="4.5" fill="none" stroke="var(--red)"/><path d="M1 36 L4 39 L7 36" fill="none" stroke="var(--red)"/>
</svg>
<p class="abs foot-text" style="left:71px;top:1089px">The address of our Customer Contact Centre is<br>22 Quayside Row, Dublin 2, Ireland<br>01 555 0148<br>help@brightharbour.com</p>

<h4 class="abs foot-heading" style="left:218px">Latest Tweets</h4>
<p class="abs foot-text" style="left:229px;top:1042px">Aenean lacinia bibendum nulla sed leo<br>posuere erat a ante venenatis dapibus<br><span class="foot-date">posuere velit aliquet.</span></p>
<p class="abs foot-text" style="left:229px;top:1090px">Donec ullamcorper metus auctor fringilla.<br>Nullam <span class="foot-date">quis risus eget.</span></p>
<p class="abs foot-text" style="left:229px;top:1126px"><span class="foot-date">Vestibulum id ligula</span> porta euismod<br>semper. Maecenas faucibus mollis.</p>

<h4 class="abs foot-heading" style="left:384px">Popular Posts</h4>
<p class="abs foot-text" style="left:384px;top:1042px">Vivamus sagittis lacus vel augue<br>rutrum dolor auctor.<br><span class="foot-date" style="font-size:5px">14 Nov, 2015</span></p>
<p class="abs foot-text" style="left:384px;top:1086px">Scelerisque nisl consectetur et.<br><span class="foot-date" style="font-size:5px">14 Nov, 2015</span></p>
<p class="abs foot-text" style="left:384px;top:1117px">Pellentesque ornare sem lacinia quam<br>venenatis vestibulum. Fusce dapibus,<br><span class="foot-date" style="font-size:5px">14 Nov, 2015</span></p>

<h4 class="abs foot-heading" style="left:520px">News Letter</h4>
<div class="abs field" style="left:520px;top:1046px;height:17px">Name:</div>
<div class="abs field" style="left:520px;top:1069px;height:17px">Email:</div>
<div class="abs field" style="left:520px;top:1092px;height:31px">Message:</div>
<div class="abs btn-submit">SUBMIT</div>

<div class="abs foot-bottom"></div>
<div class="abs copyright">© Copyright 2015 Bright Harbour .All Right Reserved.</div>
<span class="abs social" style="left:553px"></span>
<span class="abs social" style="left:574px"></span>
<span class="abs social" style="left:595px"></span>
<span class="abs social" style="left:616px"></span>
</body>
</html>
```